Fatigued and Overloaded by COVID Messages? We need original illustrations to show that.

Everywhere you look there are messages about COVID. That is leading many people to feel fatigued and overloaded by the messages.

We surveyed U.S. adults March 20th - 24th, 2020 and measured message fatigue, information overload, perceived repetition, and perceived exaggeration. Here is how participants responded:

When it comes to coronavirus . . .
55% feel exhausted by all the messages.
54% feel overloaded by the amount of information.
51% feel that the messages are repetitive.
47% feel like messages exaggerate how bad it is.

In other words, almost half of U.S. adults show signs of message fatigue, information overload, perceived message repetition, and perceived message exaggeration.

We will continue to survey 400 adults every week for the next 16 weeks. Each time we will measure message fatigue, information overload, perceived repetition, and perceived exaggeration. We expect that it will increase over time.

What are we looking for? We need innovative and original illustrations that attempt to communicate these findings. The illustrations would visualize message fatigue, information overload, perceived message repetition, and perceived message exaggeration.

What sort of visual are we looking for? Our preference is for an original illustration (or set of illustrations). Our preference is for creative and powerful illustrations, but we are also open to the creative and well-executed infographics.

We need these images fast . We will award monetary prizes to the 3 best designs. If we like more than that, then we might purchase more (e.g., in past contests, we have purchased as many as 30 designs).

What we will need:
(1) The illustrations must be original and we will need the photoshop and/or illustrator files for all artwork. (By original, we mean that the illustrations are 100% created by you. Our organization requires that we utilize only original illustrated work. We have had issues with free imagery being pirated and reposted as free. We sidestep that issue by just having everything created.)

(2) The illustration should say, somewhere: "Based on a survey of 400 U.S. adults conducted March 20 - 24th, 2020."

(3) We will have almost 4 months worth of data by the time this is done. In other words, the illustrations might be able to help us present that weekly data.

(4) We have conducted other Artvendo projects. It might be helpful to examine designs we liked in the past. For example, here is another COVID project we just finished:

https://jobs.artvendo-example.com/job/5162048

Target Market(s)

U.S. adults

Requirements
Must have
• Original illustrations. Mobile friendly design. People will view this on their smartphones.
Nice to have
• A design that we can use to communicate the data across time.

```html
<!DOCTYPE html>
<html lang="en">
<head>
<meta charset="utf-8">
<title>Fatigued and Overloaded by COVID Messages</title>
<link rel="stylesheet" href="https://fonts.googleapis.com/css2?family=Gochi+Hand&family=Fredoka:wght@600;700&display=swap">
<style>
  :root {
    --backdrop: #2b2b2b;
    --paper: #ffffff;
    --orange: #e87f24;
    --ink: #111111;
    --ring-track: #eef0f5;
  }
  html, body { margin: 0; padding: 0; }
  body {
    width: 1200px; height: 2226px; overflow: hidden;
    background: var(--backdrop);
  }
  .infographic { display: block; width: 1200px; height: 2226px; }
  .hand { font-family: "Gochi Hand", cursive; }
  .block { font-family: "Fredoka", sans-serif; font-weight: 700; }
  .title-text { fill: var(--ink); letter-spacing: 1px; }
  .intro { fill: var(--ink); font-size: 38px; }
  .band-text { fill: var(--paper); font-size: 40px; letter-spacing: 2px; }
  .stat-num { fill: var(--paper); font-size: 64px; }
  .stat-line { fill: var(--ink); font-size: 29px; }
  .stat-key { fill: var(--paper); font-size: 32px; letter-spacing: 1.5px; }
  .divider { stroke: #f6d3b0; stroke-width: 1.5; }
  .icon { fill: none; stroke: var(--ink); stroke-width: 3.5; stroke-linecap: round; stroke-linejoin: round; }
  .underline { stroke: var(--ink); stroke-width: 2; }
  .summary { fill: var(--orange); font-size: 29px; }
  .note { fill: var(--paper); font-size: 21px; }
  .ring-label { fill: var(--orange); font-size: 50px; }
</style>
</head>
<body>
<svg class="infographic" viewBox="0 0 1200 2226" xmlns="http://www.w3.org/2000/svg">
  <defs>
    <linearGradient id="illo-tone" x1="0" y1="0" x2="1" y2="1">
      <stop offset="0" stop-color="#fbe6d2"/>
      <stop offset="1" stop-color="#e9e9e9"/>
    </linearGradient>
  </defs>

  <!-- Poster sheet -->
  <rect class="sheet" x="150" y="56" width="893" height="2092" fill="var(--paper)"/>

  <!-- Header illustration area -->
  <rect x="205" y="100" width="800" height="635" fill="url(#illo-tone)" role="img"
        aria-label="Illustration of an overwhelmed man with a tiny figure shouting into a megaphone beside his head, surrounded by virus particles, clouds, a laptop, a phone and a clock"/>

  <!-- Title speech bubble -->
  <path d="M705 150 C780 105 930 110 985 160 C1030 205 1025 330 990 380 C950 430 830 435 760 410 C700 400 640 410 575 385 C630 380 660 360 665 330 C640 280 640 200 705 150 Z"
        fill="var(--orange)"/>
  <text class="block title-text" x="735" y="200" font-size="33" textLength="248" lengthAdjust="spacingAndGlyphs">FATIGUED AND</text>
  <text class="block title-text" x="690" y="248" font-size="33" textLength="293" lengthAdjust="spacingAndGlyphs">OVERLOADED BY</text>
  <text class="block title-text" x="812" y="310" font-size="56" textLength="168" lengthAdjust="spacingAndGlyphs">COVID</text>
  <text class="block title-text" x="701" y="372" font-size="56" textLength="279" lengthAdjust="spacingAndGlyphs">MESSAGES</text>

  <!-- Survey panel -->
  <path d="M195 738 L1000 733 L1002 1100 L998 1668 L196 1672 L199 1200 Z" fill="var(--orange)"/>

  <text class="hand intro" x="234" y="807" textLength="728" lengthAdjust="spacingAndGlyphs">Based on a survey of 400 U.S. adults conducted</text>
  <text class="hand intro" x="234" y="862" textLength="373" lengthAdjust="spacingAndGlyphs">March 20 - 24th, 2020:</text>

  <text class="hand intro" x="234" y="946" textLength="267" lengthAdjust="spacingAndGlyphs">When it comes to</text>
  <path d="M520 902 L935 898 L946 935 L938 966 L515 970 L508 936 Z" fill="var(--ink)"/>
  <text class="block band-text" x="548" y="948" textLength="362" lengthAdjust="spacingAndGlyphs">CORONAVIRUS . . .</text>

  <!-- Row 1 -->
  <polygon points="334,956 356,988 398,972 392,1012 428,1030 392,1052 402,1094 358,1082 336,1126 314,1086 270,1098 280,1056 244,1034 282,1012 274,972 314,988"
           fill="var(--ink)"/>
  <text class="block stat-num" x="260" y="1064" textLength="150" lengthAdjust="spacingAndGlyphs">55%</text>
  <g class="icon">
    <rect x="476" y="1012" width="88" height="64"/>
    <path d="M476 1012 L520 1050 L564 1012"/>
    <rect x="492" y="996" width="56" height="36"/>
    <path d="M502 1008 H538 M502 1018 H530"/>
    <path d="M462 1040 V1070 M572 1006 L580 1020"/>
  </g>
  <text class="hand stat-line" x="618" y="1041" textLength="41" lengthAdjust="spacingAndGlyphs">feel</text>
  <text class="block stat-key" x="666" y="1041" textLength="194" lengthAdjust="spacingAndGlyphs">EXHAUSTED</text>
  <text class="hand stat-line" x="618" y="1083" textLength="217" lengthAdjust="spacingAndGlyphs">by all the messages.</text>
  <line class="underline" x1="668" y1="1089" x2="830" y2="1087"/>
  <line class="divider" x1="223" y1="1126" x2="969" y2="1126"/>

  <!-- Row 2 -->
  <polygon points="334,1128 360,1160 408,1142 398,1186 446,1206 400,1230 414,1276 362,1262 338,1298 312,1262 262,1274 272,1230 208,1210 270,1186 262,1142 310,1160"
           fill="var(--ink)"/>
  <text class="block stat-num" x="260" y="1236" textLength="150" lengthAdjust="spacingAndGlyphs">54%</text>
  <g class="icon">
    <path d="M470 1184 V1262 H586"/>
    <rect x="482" y="1236" width="12" height="22"/>
    <rect x="502" y="1226" width="12" height="32"/>
    <rect x="522" y="1214" width="12" height="44"/>
    <rect x="542" y="1200" width="12" height="58"/>
    <rect x="562" y="1188" width="12" height="70"/>
    <path d="M494 1202 L526 1174 L540 1188 L566 1160 M552 1160 H568 V1176"/>
  </g>
  <text class="hand stat-line" x="618" y="1223" textLength="41" lengthAdjust="spacingAndGlyphs">feel</text>
  <text class="block stat-key" x="670" y="1223" textLength="216" lengthAdjust="spacingAndGlyphs">OVERLOADED</text>
  <text class="hand stat-line" x="895" y="1223" textLength="27" lengthAdjust="spacingAndGlyphs">by</text>
  <text class="hand stat-line" x="618" y="1264" textLength="291" lengthAdjust="spacingAndGlyphs">the amount of information.</text>
  <line class="underline" x1="690" y1="1270" x2="838" y2="1268"/>
  <line class="divider" x1="223" y1="1299" x2="969" y2="1299"/>

  <!-- Row 3 -->
  <polygon points="330,1304 352,1332 394,1318 388,1358 422,1380 390,1404 400,1446 356,1432 336,1470 314,1434 272,1444 280,1404 246,1380 280,1358 274,1318 312,1334"
           fill="var(--ink)"/>
  <text class="block stat-num" x="260" y="1408" textLength="140" lengthAdjust="spacingAndGlyphs">51%</text>
  <g class="icon">
    <path d="M446 1374 H518 V1414 H478 L462 1430 V1414 H446 Z"/>
    <path d="M500 1396 H570 V1434 H556 V1450 L540 1434 H500 Z"/>
    <path d="M462 1394 L470 1388 L478 1396 L486 1388 L494 1394"/>
    <path d="M508 1366 L516 1348 L526 1360 L536 1340 L546 1360 L558 1352 L574 1380"/>
  </g>
  <text class="hand stat-line" x="618" y="1407" textLength="249" lengthAdjust="spacingAndGlyphs">feel that the messages</text>
  <line class="underline" x1="762" y1="1413" x2="867" y2="1411"/>
  <text class="hand stat-line" x="618" y="1452" textLength="33" lengthAdjust="spacingAndGlyphs">are</text>
  <text class="block stat-key" x="657" y="1452" textLength="187" lengthAdjust="spacingAndGlyphs">REPETITIVE</text>
  <text class="hand stat-line" x="846" y="1452">.</text>
  <line class="divider" x1="223" y1="1480" x2="969" y2="1480"/>

  <!-- Row 4 -->
  <polygon points="330,1478 356,1512 404,1494 396,1538 440,1560 396,1584 410,1628 360,1614 336,1652 312,1614 262,1628 270,1584 218,1562 270,1538 264,1494 310,1512"
           fill="var(--ink)"/>
  <text class="block stat-num" x="260" y="1586" textLength="150" lengthAdjust="spacingAndGlyphs">47%</text>
  <g class="icon">
    <path d="M460 1560 L530 1534 V1614 L460 1590 Z"/>
    <rect x="446" y="1560" width="14" height="30"/>
    <path d="M468 1592 L474 1624 H490 L486 1598"/>
    <path d="M548 1546 L580 1530 M552 1574 H586 M548 1602 L580 1618"/>
  </g>
  <text class="hand stat-line" x="618" y="1562" textLength="196" lengthAdjust="spacingAndGlyphs">feel like messages</text>
  <text class="block stat-key" x="616" y="1605" textLength="219" lengthAdjust="spacingAndGlyphs">EXAGGERATE</text>
  <text class="hand stat-line" x="845" y="1605" textLength="140" lengthAdjust="spacingAndGlyphs">how bad it is.</text>
  <line class="underline" x1="862" y1="1612" x2="968" y2="1610"/>

  <!-- Summary panel -->
  <path d="M196 1700 L1002 1697 L1000 2000 L998 2097 L196 2100 L198 1900 Z" fill="var(--ink)"/>
  <text class="hand summary" x="243" y="1781" textLength="447" lengthAdjust="spacingAndGlyphs">In other words, almost half of U.S. adults</text>
  <text class="hand summary" x="243" y="1820" textLength="466" lengthAdjust="spacingAndGlyphs">show signs of message fatigue, information</text>
  <text class="hand summary" x="243" y="1859" textLength="425" lengthAdjust="spacingAndGlyphs">overload, perceived message repetition,</text>
  <text class="hand summary" x="243" y="1898" textLength="397" lengthAdjust="spacingAndGlyphs">and perceived message exaggeration.</text>

  <g class="ring">
    <circle cx="848" cy="1825" r="78" fill="none" stroke="var(--ring-track)" stroke-width="22"/>
    <path d="M848 1747 A78 78 0 0 1 848 1903" fill="none" stroke="var(--orange)" stroke-width="22"/>
    <text class="block ring-label" x="795" y="1843" textLength="109" lengthAdjust="spacingAndGlyphs">50%</text>
  </g>

  <text class="hand note" x="243" y="1970" textLength="681" lengthAdjust="spacingAndGlyphs">We will continue to survey 400 adults every week for the next 16 weeks. Each time</text>
  <text class="hand note" x="243" y="2000" textLength="675" lengthAdjust="spacingAndGlyphs">we will measure message fatigue, information overload, perceived repetition, and</text>
  <text class="hand note" x="243" y="2030" textLength="542" lengthAdjust="spacingAndGlyphs">perceived exaggeration. We expect that it will increase over time.</text>
</svg>
</body>
</html>
```